Charitable and Benefit Event Auctioneer and Emcee

My name is Wes
People know me as Wes The Auctioneer
My email is westheauctioneer@...
Include Phone number
This is a very unique and distinct type of Auctioneering that focuses on high profile charitable events including black tie galas, fundraisers and golf tournaments...
Clients include hospitals, schools, service agencies, corporations, foundations
Event consultation is also offered
Graduate of The Brightwater Valley School of Auctioneering
in the Fundraising Auction business since 1998

Reason: I have been too busy to give time to appropriate time to the designs submitted and I'm still having learning challenges with the pixelguild website.

Target Market(s)

Very high profile nonprofit organizations hosting gala events raising millions of dollars.

Industry/Entity Type

Events

Font styles to use
Sans Serif

Colors

Designer to choose colors to be used in the design.

Requirements
Must have
• Classy, eye catching, unique.

```html
<!DOCTYPE html>
<html lang="en">
<head>
<meta charset="utf-8">
<title>Wes The Auctioneer – Business Card</title>
<link href="https://fonts.googleapis.com/css2?family=Roboto:wght@500&display=swap" rel="stylesheet">
<style>
  :root {
    --page-bg: #e8e5e1;
    --card-black: #0b0b0c;
    --accent-red: #e8323f;
    --accent-red-light: #f25562;
    --text-white: #f4f4f4;
    --fold-white: #ffffff;
    --fold-shadow: #8e1a23;
  }
  * { margin: 0; padding: 0; box-sizing: border-box; }
  html, body {
    width: 1200px; height: 900px; overflow: hidden;
    background: var(--page-bg);
  }
  .canvas { position: relative; width: 1200px; height: 900px; }

  .card {
    position: absolute; left: 300px;
    width: 600px; height: 343px;
    background: var(--card-black);
    border-radius: 14px;
    overflow: hidden;
    box-shadow: 0 10px 28px rgba(0,0,0,.25);
  }
  .card--front { top: 60px; }
  .card--back  { top: 480px; }

  .rule {
    position: absolute; left: 0; right: 0; height: 3px;
    background: var(--accent-red);
  }
  .card--front .rule--top { top: 22px; }
  .card--front .rule--bottom { top: 286px; }
  .card--back .rule--top { top: 28px; }
  .card--back .rule--bottom { top: 300px; }

  .brand {
    position: absolute;
    display: flex; align-items: center;
    font-family: "Roboto", sans-serif; font-weight: 500;
    color: var(--text-white);
    white-space: nowrap;
    line-height: 1;
  }
  .brand__mark { flex: none; background: var(--accent-red); }

  .card--front .brand { left: 70px; top: 130px; gap: 16px; font-size: 42px; }
  .card--front .brand__mark { width: 30px; height: 30px; }

  .card--back .brand { left: 36px; top: 186px; gap: 8px; font-size: 20px; }
  .card--back .brand__mark { width: 14px; height: 14px; }

  .contact-panel {
    position: absolute; left: 318px; top: 31px;
    width: 246px; height: 222px;
    background: linear-gradient(160deg, var(--accent-red-light), var(--accent-red));
  }
  .contact-panel__fold {
    position: absolute; right: 0; top: 0; width: 40px; height: 40px;
  }
  .contact-list {
    position: absolute; left: 16px; bottom: 74px;
    list-style: none;
    font-family: "Roboto", sans-serif; font-weight: 500;
    font-size: 12.5px; color: var(--text-white);
  }
  .contact-list li { display: flex; align-items: center; gap: 7px; margin-top: 4px; }
  .contact-list svg { width: 11px; height: 11px; flex: none; }
</style>
</head>
<body>
<main class="canvas">

  <section class="card card--front" aria-label="Card front">
    <span class="rule rule--top"></span>
    <h1 class="brand">
      <span class="brand__mark" aria-hidden="true"></span>
      Wes The Auctioneer
    </h1>
    <span class="rule rule--bottom"></span>
  </section>

  <section class="card card--back" aria-label="Card back">
    <span class="rule rule--top"></span>
    <div class="contact-panel">
      <svg class="contact-panel__fold" viewBox="0 0 40 40" aria-hidden="true">
        <polygon points="0,0 40,0 40,40" fill="var(--card-black)"/>
        <polygon points="0,0 40,40 4,40" fill="var(--fold-shadow)" opacity=".55"/>
        <polygon points="0,0 40,40 0,40" fill="var(--fold-white)"/>
      </svg>
      <ul class="contact-list">
        <li>
          <svg viewBox="0 0 24 24" aria-hidden="true"><path fill="#fff" d="M6.6 10.8a15.1 15.1 0 0 0 6.6 6.6l2.2-2.2a1 1 0 0 1 1-.25 11.4 11.4 0 0 0 3.6.57 1 1 0 0 1 1 1V20a1 1 0 0 1-1 1A17 17 0 0 1 3 4a1 1 0 0 1 1-1h3.5a1 1 0 0 1 1 1c0 1.25.2 2.45.57 3.57a1 1 0 0 1-.25 1z"/></svg>
          555-010-4827
        </li>
        <li>
          <svg viewBox="0 0 24 24" aria-hidden="true"><path fill="#fff" d="M2 5h20v14H2z"/><path d="M2 5l10 8 10-8" fill="none" stroke="#e8323f" stroke-width="2"/></svg>
          westheauctioneer@maplemail.ca
        </li>
      </ul>
    </div>
    <div class="brand">
      <span class="brand__mark" aria-hidden="true"></span>
      Wes The Auctioneer
    </div>
    <span class="rule rule--bottom"></span>
  </section>

</main>
</body>
</html>
```